Book Cover: Dissolving The Hollow Mandate with KEEL-Route

I'm looking for a book cover for my pending book. I do NOT want any AI-generated image with its notoriously-slick AI imagery.
The Title is: "Dissolving The Hollow Mandate with KEEL-Route" with the lengthy added subtitle "The Lantern Method for Steadily Mending Civic Foundations, Apart from Partisan Contests, Within Mere Weeks."
Also on the front cover--author name of "Dale Voskuhl" (lower on the cover).
Parameters or things to consider:
1. Please separate the title from the subtitle with a colon, and emphasize the title greatly over the long subtitle.
2. "The Hollow Mandate" is ultimately a "bad" thing (because it cleverly hides federal action beyond the spirit of the Constitution).
3. Since abolishing a "bad" thing is a good thing, "Dissolving" should reflect that positive note, and perhaps be larger font, perhaps slanted (symbolically cancelling then "The Hollow Mandate").
4. "KEEL-Route" is a "good" thing, too, as it's the method to end the bad thing.
5. On the subtitle, much smaller fonts to keep all that text from overwhelming the front cover.
6. Please allow 3/8" for bleed and then still keep all text well away (3/8" or more) from those trim edges.
7. The book will be 6" X 9", and probably 1" thick (~400 pages). Overall dimensions will be 13.75" WX 9 .75" H (again, 3/8" bleed X 4).
8. For the back cover, but I'll just put a white box over most of the back, and then add the text later (before print submission). Continue colors of front onto back (but no real graphic needed).
9. For the cover graphic, I was thinking that an old country road may work well, because of the relevance of the fictional metaphor that is found in Chapter 3 of this non-fiction book. However, I'm not sure if this image will prove successful (even as the story provides a great visual for the premise of the book).
10. Spine: Title and author last name only is fine (no subtitle or first name of author).
Basically, I'm thinking of a long-ago rural road, perhaps in Utah (fictionally), with generic red rock formations in the background, and largely desert views surrounding the roadway. The simple road itself needn't necessarily be paved, but no more than one lane in each direction and not a lot of modern street markings.
I prefer the approach road to the T-Intersection be more-visible -- at a closer-perspective -- as it travels from the lower left of the front cover, slightly upwards, at a growing distance, towards the right side of the book, but ending well before the book's right edge, at a formal "T-Intersection," with this crossroad at 90 degrees perpendicular to the approach road.
This crossroad then will come from the (lower) right of the book, heading somewhat slantwise to the (upper) left area of the book generally, with the approach road largely hitting the crossroad largely centered at the T-Intersection, or slightly to the right of center.
There should be some sort of simple American-styled stop sign (not necessarily modern design) in the normal position, found before the crossroad, at the right lane. No vehicles.
AFTER the crossroad, at the far side of the T-Intersection, the storyline describes a solid hard-rock wall, maybe 10' or 15' high, parallel with the crossroad, but not so insurmountable that the rock wall couldn't later be excavated/demolished and partially removed, so that the approach road would later continue forward, initially at street level, but much later even with an overpass (so plan the terrain beyond the T-Intersection accordingly, that an overpass from the approach road could continue forward from the stop sign, that currently only offers a left or right path).
In-between the far side of the crossroad and the rock wall, there should be some sort of crude arrow sign, serving as a simple notice or barrier against travelling forward, notifying people to turn either right or left.
That arrow sign pointing right could also say "Enumerated Powers" and the sign pointing left can point to "Inherent Powers".
Again, the signs should be simple (more appropriate for long-ago, rather than modern).
In the story, decades later, the rock wall gets excavated first for a ground-level road, that in time became a multi-lane formal overpass and freeway, that largely ends up hiding the old T-Intersection from open view, but importantly, NEVER REMOVES OR FULLY OBSCURES the T-Intersection, or right-path road (the overpass gets shifted a little left from the approach road [with the approach road then becoming the one-way off-ramp, down to the stop sign, from the new freeway forward]).
It may be unworkable, but perhaps the primary shaded-in view would be that initial/earliest scene described above, but perhaps a stick or outline future-vision-view (like an engineering draft, for example) could overlay or outline an overpass and formal freeway continuing forward.
Again, though, the original T-Intersection can't be fully obscured or torn down with the new freeway design, even as it could be partially obscured.
I am open though, to other ideas on the cover, but I just don't know what they would be.
The design ultimately should reflect 200 years of incremental federal treachery, imposed primarily by our courts (with improper action resting upon invalid and dishonest activity [yet when properly-challenged, may be overcome {think of Pip in The Conjurer of Vell, pulling back the curtain to expose the self-proclaiming wizard of unlimited power, who was only a fraud}]).
Please note that although The Marvelous Conjurer of Vell book is now in the public domain, the 1939 movie is still copyrighted (so no visuals based on the movie), in any alternate designs.
Conservative Americans interested in restoring individual liberty and limited government under the U.S. Constitution and our country's founding principles

```html
<!DOCTYPE html>
<html lang="en">
<head>
<meta charset="utf-8">
<title>Dissolving The Hollow Mandate with KEEL-Route — Cover</title>
<link href="https://fonts.googleapis.com/css2?family=Anton&family=Oswald:wght@500;700&family=Libre+Baskerville&display=swap" rel="stylesheet">
<style>
  :root {
    --navy: #0f1a2b;
    --navy-deep: #09111d;
    --gold: #e3b45a;
    --cream: #f1ede4;
    --blue: #2f7fc4;
    --red: #a3262a;
    --author: #13213a;
    --back-top: #1d1c1c;
    --back-mid: #3a2419;
    --back-low: #7a3a17;
  }
  * { box-sizing: border-box; margin: 0; padding: 0; }
  html, body { width: 1200px; height: 800px; overflow: hidden; background: #000; }
  .cover { position: relative; width: 1200px; height: 800px; overflow: hidden; }

  /* Back cover */
  .back {
    position: absolute; left: 0; top: 0; width: 535px; height: 800px;
    background:
      radial-gradient(ellipse at 50% 40%, rgba(0,0,0,0) 30%, rgba(0,0,0,.55) 100%),
      linear-gradient(180deg, var(--back-top) 0%, var(--back-mid) 55%, var(--back-low) 100%);
  }
  .back-copy-area {
    position: absolute; left: 55px; top: 98px; width: 415px; height: 619px;
    background: #fff;
  }

  /* Spine */
  .spine {
    position: absolute; left: 535px; top: 0; width: 78px; height: 800px;
    background: linear-gradient(90deg, var(--navy-deep), var(--navy) 50%, var(--navy-deep));
    border-left: 1px solid rgba(227,180,90,.35);
  }
  .spine-text {
    position: absolute; left: 50%; top: 40px;
    transform-origin: 0 0;
    transform: translateX(28px) rotate(90deg);
    white-space: nowrap;
    display: flex; align-items: center; gap: 14px;
    width: 730px;
  }
  .spine-title-main {
    font-family: "Anton", sans-serif; font-size: 34px; color: var(--gold);
    display: inline-block; transform: skewX(-10deg); letter-spacing: 1px;
  }
  .spine-title-sub {
    font-family: "Oswald", sans-serif; font-weight: 500; color: var(--cream);
    font-size: 15px; line-height: 1.05; letter-spacing: 1.5px;
  }
  .spine-with { font-family: "Oswald", sans-serif; font-weight: 500; color: var(--cream); font-size: 15px; letter-spacing: 1.5px; }
  .spine-route { font-family: "Oswald", sans-serif; font-weight: 700; color: var(--blue); font-size: 26px; letter-spacing: 1px; }
  .spine-divider { width: 2px; height: 16px; background: var(--red); }
  .spine-author { font-family: "Oswald", sans-serif; font-weight: 700; color: var(--gold); font-size: 24px; letter-spacing: 2px; }

  /* Front cover */
  .front { position: absolute; left: 613px; top: 0; width: 587px; height: 800px; }
  .front-scene {
    position: absolute; inset: 0;
    background:
      radial-gradient(ellipse at 85% 45%, rgba(240,160,70,.75) 0%, rgba(200,110,40,.35) 30%, rgba(0,0,0,0) 60%),
      linear-gradient(180deg, #1b2434 0%, #2c3646 30%, #6a5138 52%, #8d6b45 62%, #9a7349 75%, #b38a5c 100%);
  }
  .front-type { position: absolute; inset: 0; text-align: center; }
  .title-dissolving {
    position: absolute; left: 0; right: 0; top: 58px;
    font-family: "Anton", sans-serif; font-size: 98px; line-height: 1;
    color: var(--gold); letter-spacing: 1px;
    transform: skewX(-10deg);
    text-shadow: 2px 3px 6px rgba(0,0,0,.6);
  }
  .title-rule {
    position: absolute; left: 105px; right: 105px;
    display: flex; align-items: center; justify-content: center; gap: 14px;
    font-family: "Oswald", sans-serif; font-weight: 700; color: var(--cream);
    font-size: 24px; letter-spacing: 3px;
  }
  .title-rule::before, .title-rule::after { content: ""; flex: 1; height: 2px; background: var(--red); }
  .title-rule.the { top: 172px; }
  .title-rule.with { top: 344px; }
  .title-mandate {
    position: absolute; left: 0; right: 0; top: 200px;
    font-family: "Oswald", sans-serif; font-weight: 700; color: var(--cream);
    font-size: 66px; line-height: 1.02; letter-spacing: 3px;
    text-shadow: 2px 3px 6px rgba(0,0,0,.55);
  }
  .title-route {
    position: absolute; left: 0; right: 0; top: 368px;
    font-family: "Oswald", sans-serif; font-weight: 700; color: var(--blue);
    font-size: 58px; line-height: 1; letter-spacing: 4px;
    text-shadow: 2px 2px 5px rgba(0,0,0,.5);
  }
  .subtitle {
    position: absolute; left: 90px; right: 90px; top: 436px;
    font-family: "Libre Baskerville", serif; font-size: 13.5px; line-height: 1.3;
    color: var(--cream); text-shadow: 1px 1px 3px rgba(0,0,0,.7);
  }
  .author-block { position: absolute; left: 0; right: 0; top: 710px; }
  .author-rule { display: flex; align-items: center; justify-content: center; gap: 8px; }
  .author-rule::before, .author-rule::after { content: ""; width: 70px; height: 2px; background: var(--red); }
  .author-rule svg { width: 10px; height: 10px; }
  .author-name {
    font-family: "Oswald", sans-serif; font-weight: 700; color: var(--author);
    font-size: 40px; letter-spacing: 4px; line-height: 1.15; margin: 2px 0;
  }
</style>
</head>
<body>
<div class="cover">
  <section class="back">
    <div class="back-copy-area"></div>
  </section>

  <section class="spine">
    <div class="spine-text">
      <span class="spine-title-main">DISSOLVING</span>
      <span class="spine-title-sub">THE HOLLOW<br>MANDATE</span>
      <span class="spine-with">WITH</span>
      <span class="spine-route">KEEL-ROUTE</span>
      <span class="spine-divider"></span>
      <span class="spine-author">VOSKUHL</span>
    </div>
  </section>

  <section class="front">
    <div class="front-scene" role="img" aria-label="Dusky desert landscape under a dramatic sunset sky: a dirt road leading to a T-intersection with a stop sign, crude wooden arrow signs reading Inherent Powers and Enumerated Powers before a rock wall, and an outlined future overpass sweeping in from the right"></div>
    <div class="front-type">
      <h1>
        <span class="title-dissolving">DISSOLVING</span>
        <span class="title-rule the">THE</span>
        <span class="title-mandate">HOLLOW<br>MANDATE</span>
        <span class="title-rule with">WITH</span>
        <span class="title-route">KEEL-ROUTE</span>
      </h1>
      <p class="subtitle">The Lantern Method for Steadily Mending Civic Foundations, Apart from Partisan Contests, Within Mere Weeks.</p>
      <div class="author-block">
        <div class="author-rule"><svg viewBox="0 0 10 10"><polygon points="5,0 6.2,3.8 10,3.8 6.9,6.1 8.1,10 5,7.6 1.9,10 3.1,6.1 0,3.8 3.8,3.8" fill="#a3262a"/></svg></div>
        <p class="author-name">DALE VOSKUHL</p>
        <div class="author-rule"><svg viewBox="0 0 10 10"><polygon points="5,0 6.2,3.8 10,3.8 6.9,6.1 8.1,10 5,7.6 1.9,10 3.1,6.1 0,3.8 3.8,3.8" fill="#a3262a"/></svg></div>
      </div>
    </div>
  </section>
</div>
</body>
</html>
```